Notepads for Marketing pieces-BOLD design

Looking for notepads for marketing pieces with logo, phone number, and website. Maybe something faded in background. Looking for bold and different

```html
<!DOCTYPE html>
<html lang="en">
<head>
<meta charset="utf-8">
<title>Vitalon Care Notepad</title>
<link rel="stylesheet" href="https://fonts.googleapis.com/css2?family=Antonio:wght@600&family=Inter:wght@500&family=Oswald:wght@600&display=swap">
<style>
  :root {
    --backdrop: #978f84;
    --paper: #ffffff;
    --brand-red: #d32027;
    --brand-black: #050608;
    --rule: #e6e6e6;
    --ghost-red: rgba(211, 32, 39, 0.07);
    --white: #ffffff;
  }
  * { margin: 0; padding: 0; box-sizing: border-box; }
  html, body { width: 1200px; height: 764px; overflow: hidden; }
  body { background: var(--backdrop); position: relative; }

  .notepad {
    position: absolute; left: 364px; top: 77px;
    width: 471px; height: 610px;
    background: var(--paper); overflow: hidden;
  }
  .notepad-shapes { position: absolute; inset: 0; }

  .brand-name {
    position: absolute; left: 0; width: 360px; top: 28px;
    text-align: center;
    font-family: "Oswald", sans-serif; font-weight: 600;
    font-size: 34px; letter-spacing: 1px; line-height: 1;
    color: var(--white);
  }
  .service-line {
    position: absolute; left: 0; width: 360px; top: 85px;
    text-align: center;
    font-family: "Inter", sans-serif; font-weight: 500;
    font-size: 9.4px; color: var(--white);
  }
  .service-line .divider {
    display: inline-block; width: 1.5px; height: 10px;
    background: var(--brand-red); margin: 0 4px; vertical-align: -1.5px;
  }

  .ghost-name {
    position: absolute; left: 60px; top: 210px; width: 350px;
    font-family: "Oswald", sans-serif; font-weight: 600;
    font-size: 96px; line-height: 1.15; text-align: center;
    color: var(--ghost-red);
  }

  .footer-item {
    position: absolute; top: 572px; height: 20px;
    display: flex; align-items: center; gap: 8px;
    font-family: "Antonio", sans-serif; font-weight: 600;
    font-size: 12px; color: var(--white); white-space: nowrap;
  }
  .footer-phone { left: 20px; gap: 16px; }
  .footer-web { left: 165px; }
  .footer-mission { left: 324px; gap: 7px; font-size: 11px; }
</style>
</head>
<body>
<main class="notepad">
  <svg class="notepad-shapes" width="471" height="610" viewBox="0 0 471 610" aria-hidden="true">
    <polygon points="0,0 320,0 382,93 366,93 348,113 0,113" fill="var(--brand-black)"/>
    <polygon points="0,113 348,113 341,121 0,121" fill="var(--brand-red)"/>
    <polygon points="330,0 471,0 471,92 391,92" fill="var(--brand-red)"/>
    <polygon points="368,101 471,101 471,115 378,115 373,121 357,121" fill="var(--brand-red)"/>
    <g class="heart-icon" fill="none" stroke="var(--white)" stroke-width="1.2" stroke-linejoin="round">
      <path d="M418,79 L389,50 C378,39 383,19 399,19 C408,19 414,25 418,30 C422,25 428,19 437,19 C453,19 458,39 447,50 Z"/>
      <polyline points="385,52 400,52 404,60 407,36 410,65 413,47 416,55 420,55 423,45 426,55 431,55 434,34 437,62 440,52 452,52"/>
    </g>
    <g class="writing-rules" stroke="var(--rule)" stroke-width="1">
      <line x1="24" y1="141" x2="448" y2="141"/><line x1="24" y1="163" x2="448" y2="163"/>
      <line x1="24" y1="185" x2="448" y2="185"/><line x1="24" y1="207" x2="448" y2="207"/>
      <line x1="24" y1="229" x2="448" y2="229"/><line x1="24" y1="251" x2="448" y2="251"/>
      <line x1="24" y1="273" x2="448" y2="273"/><line x1="24" y1="295" x2="448" y2="295"/>
      <line x1="24" y1="317" x2="448" y2="317"/><line x1="24" y1="339" x2="448" y2="339"/>
      <line x1="24" y1="361" x2="448" y2="361"/><line x1="24" y1="383" x2="448" y2="383"/>
      <line x1="24" y1="405" x2="448" y2="405"/><line x1="24" y1="427" x2="448" y2="427"/>
      <line x1="24" y1="449" x2="448" y2="449"/><line x1="24" y1="471" x2="448" y2="471"/>
      <line x1="24" y1="493" x2="448" y2="493"/><line x1="24" y1="515" x2="448" y2="515"/>
      <line x1="24" y1="537" x2="448" y2="537"/>
    </g>
    <polygon points="0,554 162,554 134,610 0,610" fill="var(--brand-red)"/>
    <polygon points="166,554 314,554 286,610 138,610" fill="var(--brand-black)"/>
    <polygon points="318,554 471,554 471,610 290,610" fill="var(--brand-red)"/>
  </svg>

  <div class="ghost-name" aria-hidden="true">VITALON<br>CARE</div>

  <h1 class="brand-name">VITALON CARE</h1>
  <p class="service-line">Home Health<span class="divider"></span>Medical Staffing<span class="divider"></span>Outpatient Therapy</p>

  <div class="footer-item footer-phone">
    <svg width="15" height="15" viewBox="0 0 16 16" aria-hidden="true">
      <circle cx="8" cy="8" r="8" fill="var(--white)"/>
      <path d="M5.2,3.8 L6.6,3.6 L7.3,5.8 L6.4,6.6 C6.9,7.8 7.9,8.8 9.1,9.4 L9.9,8.5 L12,9.2 L11.8,10.6 C9,11.3 4.5,7 5.2,3.8 Z" fill="var(--brand-red)"/>
    </svg>
    <span>(555) 010-2468</span>
  </div>
  <div class="footer-item footer-web">
    <svg width="14" height="14" viewBox="0 0 16 16" aria-hidden="true" fill="none" stroke="var(--white)" stroke-width="1.2">
      <circle cx="8" cy="8" r="7"/><ellipse cx="8" cy="8" rx="3" ry="7"/>
      <line x1="1" y1="8" x2="15" y2="8"/><line x1="2.5" y1="4.5" x2="13.5" y2="4.5"/><line x1="2.5" y1="11.5" x2="13.5" y2="11.5"/>
    </svg>
    <span>www.vitaloncare.com</span>
  </div>
  <div class="footer-item footer-mission">
    <svg width="20" height="12" viewBox="0 0 22 13" aria-hidden="true" fill="var(--white)">
      <circle cx="11" cy="3" r="2.8"/><path d="M5.5,13 C5.5,8 16.5,8 16.5,13 Z"/>
      <circle cx="4" cy="5" r="2.2"/><path d="M0,13 C0,9 6,8.5 6.5,10 L5.5,13 Z"/>
      <circle cx="18" cy="5" r="2.2"/><path d="M22,13 C22,9 16,8.5 15.5,10 L16.5,13 Z"/>
    </svg>
    <span>YOUR HEALTH OUR MISSION</span>
  </div>
</main>
</body>
</html>
```